Revamp QuillStoneKit.com

https://quillstonekit.com/ needs a revamp. We like the general style and colors of the site, we just want to modernize the landing page, product page, view cart page, and the final confirm page.

I'm just looking for the PSD (Photoshop files) as the deliverable.

Quick Summary
Please redesign the following Pages:
1) https://quillstonekit.com/
2) https://quillstonekit.com/rubberTracks/QuillStoneKit/400x725nx70.php (product Page)
3) https://quillstonekit.com/viewCart.php (view cart - Add something to cart to see)
4) https://quillstonekit.com/confirmShoppingCart.php (confirm cart - Add something to cart to see)

```html
<!DOCTYPE html>
<html lang="en">
<head>
<meta charset="utf-8">
<title>Shopping Cart – QuillStoneKit</title>
<link href="https://fonts.googleapis.com/css2?family=League+Gothic&family=Lato:wght@400;700&display=swap" rel="stylesheet">
<style>
  :root {
    --cream: #f5efe2;
    --band: #eadcbc;
    --peach: #f3dbcc;
    --paper: #f8f5ee;
    --orange: #f26b4e;
    --gold: #d9a93a;
    --ink: #2e2e2e;
    --grey: #666;
    --footer: #333333;
    --tile: #555555;
  }
  * { box-sizing: border-box; margin: 0; padding: 0; }
  html, body { width: 743px; height: 1200px; overflow: hidden; }
  body { background: var(--cream); font-family: 'Lato', sans-serif; color: var(--ink); position: relative; }
  .abs { position: absolute; }
  .display { font-family: 'League Gothic', 'Oswald', sans-serif; letter-spacing: .3px; line-height: 1; }

  /* header */
  .brand { left: 42px; top: 38px; font-size: 28px; color: var(--ink); }
  .brand-mark { left: 84px; top: 16px; width: 20px; height: 20px; background: var(--ink); border-radius: 50%; }
  .util { top: 13px; font-size: 16px; color: var(--gold); display: flex; align-items: center; gap: 10px; }
  .util .ico { width: 24px; height: 21px; background: #f1dfae; border-radius: 3px; display: flex; align-items: center; justify-content: center; }
  .nav { top: 53px; left: 418px; display: flex; gap: 15px; font-size: 19px; }
  .search-ico { left: 672px; top: 52px; }

  .title-band { left: 0; top: 119px; width: 743px; height: 55px; background: var(--band); }
  .page-title { left: 72px; top: 134px; font-size: 28px; color: #3a3a3a; }

  .total { left: 476px; top: 199px; font-size: 24px; display: flex; align-items: baseline; gap: 12px; }
  .total .dollar { font-size: 28px; }
  .total .amount { font-size: 40px; color: var(--orange); margin-left: -6px; }
  .final { left: 551px; top: 238px; font-size: 23px; }

  /* cart card */
  .cart-card { left: 91px; top: 275px; width: 549px; height: 296px; background: var(--peach); border-radius: 7px; }
  .cart-head { left: 121px; top: 293px; font-size: 18px; }
  .product-img { left: 140px; top: 339px; width: 127px; height: 142px; border-radius: 30px; background: linear-gradient(135deg, #3a3a3a, #1e1e1e); }
  .delivery { left: 386px; top: 331px; font-size: 28px; color: var(--orange); }
  .dates { left: 386px; top: 371px; font-size: 29px; color: var(--orange); }
  .item-type { left: 388px; top: 410px; width: 175px; text-align: center; font-size: 24px; }
  .item-size { left: 388px; top: 438px; width: 175px; text-align: center; font-size: 24px; font-weight: bold; }
  .remove { left: 388px; top: 470px; width: 175px; text-align: center; font-size: 8px; font-weight: 700; color: #c8352a; text-decoration: underline; }
  .qty-label { left: 170px; top: 514px; width: 86px; text-align: center; font-size: 9px; font-weight: 700; color: #444; }
  .qty { left: 174px; top: 530px; width: 77px; height: 23px; display: flex; border-radius: 2px; overflow: hidden; font-size: 11px; font-weight: 700; color: #fff; }
  .qty span { display: flex; align-items: center; justify-content: center; }
  .qty .step { width: 19px; background: #6a6a6a; }
  .qty .val { flex: 1; background: #3c3c3c; }
  .line-price { left: 409px; top: 506px; display: flex; align-items: baseline; gap: 8px; }
  .line-price .dollar { font-size: 30px; }
  .line-price .amount { font-size: 42px; color: var(--orange); }

  /* shipping */
  .ship-card { left: 91px; top: 615px; width: 549px; height: 250px; background: var(--paper); border-radius: 7px 7px 0 0; }
  .truck { left: 112px; top: 636px; }
  .ship-title { left: 163px; top: 638px; font-size: 25px; }
  .ship-brand { left: 518px; top: 652px; font-size: 15px; }
  .ship-mark { left: 552px; top: 631px; width: 12px; height: 12px; background: var(--ink); border-radius: 50%; }
  .field { border-bottom: 1.5px solid #6b6b6b; font-size: 9px; color: #555; padding: 0 0 3px 8px; }
  .confirm { left: 90px; top: 852px; width: 550px; height: 32px; background: var(--orange); border-radius: 6px; color: #fff; font-size: 20px; display: flex; align-items: center; justify-content: center; }

  /* footer */
  .tread { left: 0; top: 918px; width: 743px; height: 41px; background: linear-gradient(#3d3d3d, #6a6a6a); }
  .footer { left: 0; top: 959px; width: 743px; height: 241px; background: var(--footer); }
  .foot-brand { left: 40px; top: 1030px; font-size: 44px; color: #f2f2f2; }
  .safe { top: 1111px; font-size: 12px; color: #fff; }
  .lock { left: 56px; top: 1124px; }
  .badge { top: 1129px; height: 19px; border-radius: 2px; }
  .foot-head { font-size: 22px; color: #fff; }
  .quick { left: 360px; font-size: 13px; color: #fff; }
  .search-box { left: 503px; top: 1035px; width: 199px; height: 24px; background: #fff; font-size: 10px; color: #888; padding: 6px 10px; }
  .search-btn { left: 702px; top: 1035px; width: 29px; height: 24px; background: var(--gold); display: flex; align-items: center; justify-content: center; }
  .social { top: 1083px; width: 35px; height: 35px; background: var(--tile); }
  .copyright { left: 0; top: 1180px; width: 783px; text-align: center; font-size: 11px; color: #cfcfcf; }
</style>
</head>
<body>
  <!-- header -->
  <div class="abs brand-mark"></div>
  <div class="abs brand display">QuillStoneKit</div>
  <div class="abs util display" style="left:372px">
    <span class="ico"><svg width="14" height="12" viewBox="0 0 14 12"><path d="M1 1h2l2 7h7l1-5H4" fill="none" stroke="#d9a93a" stroke-width="1.2"/><circle cx="6" cy="10.5" r="1" fill="#d9a93a"/><circle cx="11" cy="10.5" r="1" fill="#d9a93a"/></svg></span>
    CHECKOUT (0)
  </div>
  <div class="abs util display" style="left:521px">
    <span class="ico"><svg width="14" height="10" viewBox="0 0 14 10"><rect x="1" y="1" width="12" height="8" fill="none" stroke="#d9a93a"/><path d="M1 1l6 5 6-5" fill="none" stroke="#d9a93a"/></svg></span>
    SUPPORT@QUILLSTONEKIT.COM
  </div>
  <nav class="abs nav display"><span>HOME</span><span>PRODUCTS</span><span>ABOUT</span><span>CONTACT</span></nav>
  <svg class="abs search-ico" width="20" height="20" viewBox="0 0 20 20"><circle cx="8" cy="8" r="6" fill="none" stroke="#111" stroke-width="2.4"/><path d="M12.5 12.5l6 6" stroke="#111" stroke-width="2.6"/></svg>

  <div class="abs title-band"></div>
  <h1 class="abs page-title display" style="font-weight:400">SHOPPING CART</h1>

  <div class="abs total display"><span>Total:</span><span class="dollar">$</span><span class="amount">1319.75</span></div>
  <div class="abs final display">Final Price</div>

  <!-- cart -->
  <section class="abs cart-card"></section>
  <div class="abs cart-head display">SHOPPING CART (1)</div>
  <div class="abs product-img" role="img" aria-label="Photo of a black rubber replacement track loop"></div>
  <div class="abs delivery display">Expected Delivery</div>
  <div class="abs dates display">Jul 22, 2020 - Jul 29, 2020</div>
  <div class="abs item-type display">Replacement Tracks:</div>
  <div class="abs item-size display">320x86x49</div>
  <div class="abs remove">(Remove this item)</div>
  <div class="abs qty-label">Enter Quatitiy</div>
  <div class="abs qty"><span class="step">-</span><span class="val">1</span><span class="step">+</span></div>
  <div class="abs line-price display"><span class="dollar">$</span><span class="amount">1319.75</span></div>

  <!-- shipping -->
  <section class="abs ship-card"></section>
  <svg class="abs truck" width="40" height="28" viewBox="0 0 40 28" fill="none" stroke="#f26b4e" stroke-width="2.2">
    <path d="M10 4h16v16H10M26 9h6l5 6v5h-11"/><circle cx="15" cy="22" r="3.5"/><circle cx="31" cy="22" r="3.5"/>
    <path d="M1 8h7M3 12h6M1 16h7"/>
  </svg>
  <div class="abs ship-title display">Shipping Address</div>
  <div class="abs ship-mark"></div>
  <div class="abs ship-brand display">QuillStoneKit</div>

  <div class="abs field" style="left:128px;top:713px;width:184px">Name</div>
  <div class="abs field" style="left:382px;top:713px;width:184px">email@email.com</div>
  <div class="abs field" style="left:128px;top:754px;width:184px">Phone</div>
  <div class="abs field" style="left:382px;top:754px;width:184px">Company</div>
  <div class="abs field" style="left:128px;top:799px;width:184px">City</div>
  <div class="abs field" style="left:384px;top:799px;width:64px">ST</div>
  <div class="abs field" style="left:499px;top:799px;width:64px">Zip</div>

  <div class="abs confirm display">Confirm</div>

  <!-- footer -->
  <div class="abs tread" role="img" aria-label="Decorative tire tread band"></div>
  <footer class="abs footer"></footer>
  <div class="abs foot-brand display">QuillStoneKit</div>
  <div class="abs safe display" style="left:77px">Safe Payments</div>
  <div class="abs safe display" style="left:150px">Safe and Secure SSL Encrypted</div>
  <svg class="abs lock" width="21" height="25" viewBox="0 0 21 25"><path d="M5 11V7a5.5 5.5 0 0 1 11 0v4" fill="none" stroke="#000" stroke-width="2.6"/><rect x="1" y="11" width="19" height="13" rx="1" fill="#000"/></svg>
  <div class="abs badge" style="left:81px;width:67px;background:#111"></div>
  <div class="abs badge" style="left:151px;width:27px;background:#e7e7e7"></div>
  <div class="abs badge" style="left:180px;width:27px;background:#f2f2f2"></div>
  <div class="abs badge" style="left:209px;width:28px;background:#f7f7f7"></div>
  <div class="abs badge" style="left:239px;width:28px;background:#2f77c2"></div>

  <div class="abs foot-head display" style="left:360px;top:1003px">Quick Links</div>
  <div class="abs quick display" style="top:1051px">Home</div>
  <div class="abs quick display" style="top:1075px">About</div>
  <div class="abs quick display" style="top:1099px">Contact Us</div>

  <div class="abs foot-head display" style="left:562px;top:1003px">Search Tracks</div>
  <div class="abs search-box">Trackmor 325 Or 300x52.5x82</div>
  <div class="abs search-btn"><svg width="15" height="15" viewBox="0 0 20 20"><circle cx="8" cy="8" r="6" fill="none" stroke="#111" stroke-width="2.6"/><path d="M12.5 12.5l6 6" stroke="#111" stroke-width="2.8"/></svg></div>
  <div class="abs social" style="left:546px;background:var(--orange)"></div>
  <div class="abs social" style="left:597px"></div>
  <div class="abs social" style="left:648px"></div>

  <div class="abs copyright">© 2020 QuillStone Kit, LLC. All Rights are Reserved. Privacy Policy | Site Map | Terms of Service</div>
</body>
</html>
```